Homepage of voice message app

We are developing a mobile application of which one of the more important features is a voice to transcript.

What we would like to have designed is a basic interface that would show one ore more avatars on a home screen + the following functionalities:
- record
-while recording there should be three functions included in buttons (delete last sentence / send / send & next message (i.e. keep the recording going))
&
- listen (to new message)
- while listening replies should be possible in the form of emoticons (only emoticons, no text)

Attached:
-an example of the style we appreciate

Target Market(s)

English speaking Millenials

Industry/Entity Type

Messaging

Font styles to use
Sans Serif

Requirements
Must have
• My project must have a clean design and should not be too futuristic. We are targetting an average person between 20-80 years.
Nice to have
• We would like to focus on a minimum amount of finger movements to get the message across, we prefer simple tabs and swipes within the home screen to access the features.
Should not have
• The project should not have too many moving pieces within the screen.

```html
<!DOCTYPE html>
<html lang="en">
<head>
<meta charset="utf-8">
<title>Voice Message App – Screens, Flows &amp; Specs</title>
<link href="https://fonts.googleapis.com/css2?family=Inter:wght@400;500;600;700&display=swap" rel="stylesheet">
<style>
:root{
  --ink:#1b1b1b;
  --paper:#ffffff;
  --panel:#f4f4f5;
  --band-dark:#1d5b9f;
  --blue:#2f7cf5;
  --violet:#5b6df0;
  --link:#2f6fe0;
  --text:#3c3c3c;
  --line:#2b2b2b;
  --green:#39b86a;
  --key-bg:#d2d4da;
  --hint:#c7c9cf;
  --pink:#f2366f;
  --accent:#2f7cf5;
}
*{box-sizing:border-box;margin:0;padding:0}
html,body{width:1200px;height:2444px;overflow:hidden;background:var(--paper)}
body{position:relative;font-family:"Inter",sans-serif;color:var(--ink)}
.abs{position:absolute}
.title-bar{position:absolute;background:var(--ink);color:#fff;display:flex;align-items:center;font-weight:500}
.panel{position:absolute;background:var(--panel);overflow:hidden}
.panel-meta{position:absolute;left:0;right:0;top:0;background:var(--band-dark);color:#fff;font-weight:600;display:flex;align-items:center}
.panel-head{position:absolute;left:0;right:0;color:#fff;font-weight:700}
.blue .panel-head{background:var(--blue)}
.violet .panel-head{background:var(--violet)}
.panel-head h2{font-weight:700}
.spec-body h3{font-weight:500;color:#111}
.spec-body p{color:var(--text)}
.spec-body .lbl{color:#111}
.spec-body a{color:var(--link);text-decoration:none;display:block}
.arrows{position:absolute;left:0;top:0;overflow:visible}

/* phone mockups */
.ph{position:absolute;background:#fff;overflow:hidden;font-size:3px;line-height:1.2;color:#222}
.ph .sb{position:absolute;top:2%;left:6%;right:6%;display:flex;justify-content:space-between;font-size:3px;font-weight:600}
.ph .nav{position:absolute;top:7%;left:3%;right:3%;display:flex;justify-content:space-between;font-size:3px}
.ph .nav b{font-weight:600;color:#111}
.ph .nav span{color:var(--accent)}
.ph .ln{position:absolute;height:1.2%;background:#e4e5e8;border-radius:1px}
.ph .tx{position:absolute;left:0;right:0;text-align:center;font-size:3px;color:#333}
.ph .field{position:absolute;left:4%;right:4%;font-size:3.4px;color:#333;border-bottom:.4px solid #e1e1e1;padding-bottom:1px}
.ph .hint{color:var(--hint)}
.ph .blue-t{color:var(--accent)}
.ph .keys{position:absolute;left:0;right:0;bottom:0;height:35%;background:var(--key-bg);display:grid;grid-template-columns:repeat(3,1fr);gap:1.5px;padding:3px 3px 12px}
.ph .keys i{background:#fff;border-radius:1px}
.ph .qwerty{position:absolute;left:0;right:0;bottom:0;height:35%;background:var(--key-bg);display:grid;grid-template-columns:repeat(10,1fr);gap:1px;padding:3px 2px 12px}
.ph .qwerty i{background:#fff;border-radius:.5px}
.ph .home-ind{position:absolute;left:35%;right:35%;bottom:2%;height:1%;background:#111;border-radius:2px}
.ph .bubble{position:absolute;left:50%;transform:translateX(-50%);border-radius:50%;background:var(--accent)}
.ph .btn{position:absolute;left:4%;right:4%;height:5%;border-radius:2px;background:var(--accent);color:#fff;display:flex;align-items:center;justify-content:center;font-size:3px}
.ph .btn.off{background:#d9dadd}
.ph .av{position:absolute;border-radius:50%;background:#6d6f73}
.ph .av.hl{background:var(--accent)}
.ph .av.sm{background:#8a8c90}
.ph .row{position:absolute;left:4%;right:4%;display:flex;align-items:center;gap:2px;font-size:3px}
.ph .row .dot{width:5px;height:5px;border-radius:50%;background:#7a7c80;flex:none}
.ph .row .dot.b{background:var(--accent)}
.ph .row .dot.k{background:#111}
.ph .tabs{position:absolute;left:0;right:0;bottom:4%;display:flex;justify-content:space-around;align-items:center}
.ph .tabs i{width:3px;height:3px;border-radius:50%;background:#777}
.ph .tabs .rec{width:14px;height:5px;border-radius:3px;background:var(--pink)}
.ph .photo{position:absolute;inset:0;background:linear-gradient(135deg,#9fd4e8 0%,#e9a3c4 38%,#8ecbe3 62%,#f0b4cf 100%)}
.ph .emo{position:absolute;left:18%;right:18%;display:flex;justify-content:space-between}
.ph .emo i{width:5px;height:5px;border-radius:50%;background:#f4c23c}
.ph .glow{position:absolute;left:30%;width:40%;height:10%;border-radius:50%;background:radial-gradient(circle,#f7a7c6 0%,rgba(247,167,198,0) 70%)}

.note{position:absolute;background:#fff;font-size:5px;color:#333;padding:5px 6px;line-height:1.35}
.note b{font-weight:600;display:block;color:#111}
.num{position:absolute;width:9px;height:9px;border-radius:50%;background:var(--green);color:#fff;font-size:5px;font-weight:700;display:flex;align-items:center;justify-content:center}
.caption{position:absolute;font-size:5.4px;color:#333;line-height:1.3}
</style>
</head>
<body>

<!-- ============ SECTION 1: Register / Login ============ -->
<div class="title-bar" style="left:121px;top:42px;width:954px;height:60px;padding-left:23px;font-size:17px">[UI SCREEN] Register screen / Login screen: Sign up with text message (as per ChatLine)</div>

<section class="panel blue" style="left:121px;top:125px;width:614px;height:590px">
  <div class="panel-meta" style="height:16px;padding-left:20px;font-size:6px">Complete / 03.02.2021 / studio.desk@mailbox.test</div>
  <div class="panel-head" style="top:16px;height:59px;padding:7px 22px">
    <h2 style="font-size:17px">User Flows</h2>
    <p style="font-size:8px;font-weight:600;margin-top:5px;line-height:1.35">Users will be directed to register (if they do not have an account) or enter the<br>Login page if they already have an account.</p>
  </div>

  <svg class="arrows" width="614" height="590" aria-hidden="true">
    <defs><marker id="a1" viewBox="0 0 6 6" refX="5" refY="3" markerWidth="4" markerHeight="4" orient="auto"><path d="M0 0L6 3L0 6z" fill="#2b2b2b"/></marker></defs>
    <g fill="none" stroke="#2b2b2b" stroke-width=".8" marker-end="url(#a1)">
      <polyline points="96,257 122,257 122,141 150,141"/>
      <polyline points="96,258 112,258 112,198 150,198"/>
      <polyline points="219,183 232,183 232,141 273,141"/>
      <line x1="342" y1="194" x2="395" y2="194"/>
      <line x1="464" y1="194" x2="518" y2="194"/>
      <line x1="44" y1="268" x2="44" y2="323"/>
      <line x1="52" y1="323" x2="52" y2="268"/>
      <polyline points="78,268 78,334 150,334"/>
      <line x1="96" y1="398" x2="150" y2="398"/>
      <line x1="219" y1="398" x2="273" y2="398"/>
      <line x1="342" y1="398" x2="395" y2="398"/>
      <line x1="464" y1="398" x2="518" y2="398"/>
    </g>
  </svg>

  <!-- row 1 -->
  <div class="ph" style="left:27px;top:119px;width:69px;height:133px">
    <div class="photo" role="img" aria-label="Abstract pink and blue marbled background for the welcome screen"></div>
    <div class="abs" style="left:16px;top:58px;display:flex;align-items:center;gap:3px;font-size:9px;color:#fff"><i style="width:6px;height:6px;background:#fff;display:block"></i>photo</div>
  </div>
  <div class="abs" style="left:27px;top:255px;width:32px;height:10px;background:#fff;font-size:3px;color:var(--accent);display:flex;align-items:center;justify-content:center">Register</div>
  <div class="abs" style="left:65px;top:255px;width:32px;height:10px;background:var(--accent);border-radius:2px;font-size:3px;color:#fff;display:flex;align-items:center;justify-content:center">Login</div>

  <div class="ph" style="left:150px;top:119px;width:69px;height:149px">
    <div class="sb"><span>9:41</span><span>•••</span></div>
    <div class="nav"><span>‹ Back</span><b>Login</b><span class="hint">Done</span></div>
    <div class="tx" style="top:13%">Welcome back,<br>sign in to continue</div>
    <div class="field blue-t" style="top:23%;font-size:3px">United States</div>
    <div class="field" style="top:28%">+1 <span class="hint">Phone number</span></div>
    <div class="tx hint" style="top:57%">Don't have an account? <span class="blue-t">Create account</span></div>
    <div class="keys"><i></i><i></i><i></i><i></i><i></i><i></i><i></i><i></i><i></i><i></i><i></i><i></i></div>
    <div class="home-ind"></div>
  </div>
  <div class="ph" style="left:273px;top:119px;width:69px;height:149px">
    <div class="sb"><span>9:41</span><span>•••</span></div>
    <div class="nav"><span>‹ Back</span><b>Register</b><span>Done</span></div>
    <div class="tx" style="top:13%">Welcome back,<br>sign in to continue</div>
    <div class="field blue-t" style="top:23%;font-size:3px">United States</div>
    <div class="field" style="top:28%">+1 &nbsp;234 567 7</div>
    <div class="tx hint" style="top:57%">Don't have an account? <span class="blue-t">Create account</span></div>
    <div class="keys"><i></i><i></i><i></i><i></i><i></i><i></i><i></i><i></i><i></i><i></i><i></i><i></i></div>
    <div class="home-ind"></div>
  </div>
  <div class="ph" style="left:395px;top:119px;width:69px;height:149px">
    <div class="sb"><span>9:41</span><span>•••</span></div>
    <div class="nav"><span>‹ Cancel</span><b>One Time Password</b><span class="hint">Done</span></div>
    <div class="bubble" style="top:14%;width:22px;height:22px"></div>
    <div class="tx" style="top:33%;font-weight:600">Welcome to Voxlet</div>
    <div class="tx hint" style="top:38%">Enter OTP Code</div>
    <div class="tx hint" style="top:44%;font-size:4px">- - -&nbsp; - - -</div>
    <div class="tx" style="top:51%">Didn't receive any code? <span class="blue-t">Resend</span></div>
    <div class="keys"><i></i><i></i><i></i><i></i><i></i><i></i><i></i><i></i><i></i><i></i><i></i><i></i></div>
    <div class="home-ind"></div>
  </div>
  <div class="ph" style="left:518px;top:119px;width:69px;height:149px">
    <div class="sb"><span>9:41</span><span>•••</span></div>
    <div class="nav"><span>‹ Cancel</span><b>One Time Password</b><span>Done</span></div>
    <div class="bubble" style="top:14%;width:22px;height:22px"></div>
    <div class="tx" style="top:33%;font-weight:600">Welcome to Voxlet</div>
    <div class="tx hint" style="top:38%">Enter OTP Code</div>
    <div class="tx" style="top:44%;font-size:4.5px">457&nbsp; 810</div>
    <div class="tx" style="top:51%">Didn't receive any code? <span class="blue-t">Resend</span></div>
    <div class="keys"><i></i><i></i><i></i><i></i><i></i><i></i><i></i><i></i><i></i><i></i><i></i><i></i></div>
    <div class="home-ind"></div>
  </div>

  <!-- row 2 -->
  <div class="ph" style="left:27px;top:323px;width:69px;height:149px">
    <div class="sb"><span>9:41</span><span>•••</span></div>
    <div class="nav"><span>‹ Back</span><b>Register</b><span class="hint">Done</span></div>
    <div class="tx" style="top:13%">Please confirm your country code and<br>enter your phone number</div>
    <div class="field blue-t" style="top:23%;font-size:3px">United States</div>
    <div class="field" style="top:28%">+1 <span class="hint">Phone number</span></div>
    <div class="tx" style="top:57%">I agree with our <span class="blue-t">Terms and Conditions</span></div>
    <div class="keys"><i></i><i></i><i></i><i></i><i></i><i></i><i></i><i></i><i></i><i></i><i></i><i></i></div>
    <div class="home-ind"></div>
  </div>
  <div class="ph" style="left:150px;top:323px;width:69px;height:149px">
    <div class="sb"><span>9:41</span><span>•••</span></div>
    <div class="nav"><span>‹ Back</span><b>Register</b><span>Done</span></div>
    <div class="tx" style="top:13%">Please confirm your country code and<br>enter your phone number</div>
    <div class="field blue-t" style="top:23%;font-size:3px">United States</div>
    <div class="field" style="top:28%">+1 &nbsp;234 567 7</div>
    <div class="tx" style="top:57%">I agree with our <span class="blue-t">Terms and Conditions</span></div>
    <div class="keys"><i></i><i></i><i></i><i></i><i></i><i></i><i></i><i></i><i></i><i></i><i></i><i></i></div>
    <div class="home-ind"></div>
  </div>
  <div class="ph" style="left:273px;top:323px;width:69px;height:149px">
    <div class="sb"><span>9:41</span><span>•••</span></div>
    <div class="nav"><span>‹ Cancel</span><b>One Time Password</b><span>Done</span></div>
    <div class="bubble" style="top:14%;width:22px;height:22px"></div>
    <div class="tx" style="top:33%;font-weight:600">Welcome to Voxlet</div>
    <div class="tx hint" style="top:38%">Enter OTP Code</div>
    <div class="tx hint" style="top:44%;font-size:4px">- - -&nbsp; - - -</div>
    <div class="tx" style="top:51%">Didn't receive any code? <span class="blue-t">Resend</span></div>
    <div class="keys"><i></i><i></i><i></i><i></i><i></i><i></i><i></i><i></i><i></i><i></i><i></i><i></i></div>
    <div class="home-ind"></div>
  </div>
  <div class="ph" style="left:395px;top:323px;width:69px;height:149px">
    <div class="sb"><span>9:41</span><span>•••</span></div>
    <div class="nav"><span>‹ Cancel</span><b>Your Profile</b><span class="hint">Done</span></div>
    <div class="av sm" style="left:23px;top:18%;width:23px;height:23px;background:#c9cbd0"></div>
    <div class="field hint" style="top:37%">Name</div>
    <div class="btn off" style="top:54%">Done</div>
    <div class="qwerty"><i></i><i></i><i></i><i></i><i></i><i></i><i></i><i></i><i></i><i></i><i></i><i></i><i></i><i></i><i></i><i></i><i></i><i></i><i></i><i></i><i></i><i></i><i></i><i></i><i></i><i></i><i></i><i></i><i></i><i></i></div>
    <div class="home-ind"></div>
  </div>
  <div class="ph" style="left:518px;top:323px;width:69px;height:149px">
    <div class="sb"><span>9:41</span><span>•••</span></div>
    <div class="nav"><span>‹ Cancel</span><b>Your Profile</b><span>Done</span></div>
    <div class="av sm" style="left:23px;top:18%;width:23px;height:23px;background:#c9cbd0"></div>
    <div class="field" style="top:37%">Sam Porter</div>
    <div class="btn" style="top:54%">Done</div>
    <div class="qwerty"><i></i><i></i><i></i><i></i><i></i><i></i><i></i><i></i><i></i><i></i><i></i><i></i><i></i><i></i><i></i><i></i><i></i><i></i><i></i><i></i><i></i><i></i><i></i><i></i><i></i><i></i><i></i><i></i><i></i><i></i></div>
    <div class="home-ind"></div>
  </div>
  <div class="caption" style="left:395px;top:481px">- "Name" form is Required<br>- Default avatar Icon<br>&nbsp; First &amp; Last name initials</div>
</section>

<section class="panel blue" style="left:755px;top:125px;width:320px;height:590px">
  <div class="panel-meta" style="height:16px;padding-left:10px;font-size:6px">Complete / 03.02.2021 / studio.desk@mailbox.test</div>
  <div class="panel-head" style="top:16px;height:59px;padding:19px 22px">
    <h2 style="font-size:17px">Specs</h2>
  </div>
  <div class="spec-body abs" style="left:22px;top:120px;width:290px">
    <h3 style="font-size:21px">Component</h3>
    <p style="font-size:8.5px;margin-top:7px;line-height:1.35">The component should already exist within MobiOS but may not be up to scratch for Human Interface Guidelines. It's worth double checking.</p>
    <p class="lbl" style="font-size:8.5px;margin-top:13px">Details of the component can be found here:</p>
    <a style="font-size:8.5px;margin-top:3px">https://dev.mobios.test/platform/</a>
    <p class="lbl" style="font-size:8.5px;margin-top:13px">Designer Version:</p>
    <a style="font-size:8.5px;margin-top:3px">https://dev.mobios.test/design/interface-guidelines/platform</a>
  </div>
</section>

<!-- ============ SECTION 2: Permission & Search ============ -->
<div class="title-bar" style="left:171px;top:773px;width:871px;height:88px;padding-left:33px;font-size:26px">[UI SCREEN] Permission Access to contacts &amp; Search Message</div>

<section class="panel violet" style="left:171px;top:894px;width:377px;height:439px">
  <div class="panel-meta" style="height:24px;padding-left:12px;font-size:8.5px">Complete / 03.02.2021 / studio.desk@mailbox.test</div>
  <div class="panel-head" style="top:24px;height:85px;padding:30px 33px">
    <h2 style="font-size:26px">User Flows</h2>
  </div>
  <div class="ph" style="left:39px;top:184px;width:100px;height:217px;background:#d0d2d8">
    <div class="abs" style="left:13px;top:87px;width:74px;height:40px;background:#f3f3f5;border-radius:3px;font-size:3.6px;text-align:center;padding-top:4px">
      <b style="font-weight:600">"Voxlet" Would Like to<br>Access Your Contacts</b><br><span style="font-size:3px">This will be used to manage your contacts.</span>
      <div class="abs" style="left:0;right:0;bottom:0;height:10px;border-top:.5px solid #c8c8cc;display:flex;justify-content:space-around;align-items:center;color:var(--accent);font-size:3.6px"><span>Don't Allow</span><b style="font-weight:600">Allow</b></div>
    </div>
    <div class="home-ind" style="bottom:1.5%;height:1%"></div>
  </div>
  <div class="ph" style="left:226px;top:184px;width:100px;height:217px;font-size:4px">
    <div class="sb" style="font-size:4px"><span>9:41</span><span>•••</span></div>
    <div class="tx" style="top:7%;font-size:4.5px;font-weight:600">Search</div>
    <div class="abs" style="left:4%;right:4%;top:14%;height:6%;border:.5px solid #dcdcdf;border-radius:2px;font-size:3.8px;padding:2px 4px">Search message</div>
    <div class="row" style="top:23%;font-size:3.8px"><i class="dot" style="width:9px;height:9px;background:#a2563e"></i><span><b style="font-weight:600">Nora Vale</b><br><span class="hint">Start message with Nora</span></span></div>
    <div class="row" style="top:33%;font-size:3.8px"><i class="dot b" style="width:9px;height:9px"></i><span><b style="font-weight:600">Iris Kemp</b><br><span class="hint">00:24</span></span><span class="hint" style="margin-left:auto">09:01 AM</span></div>
    <div class="row" style="top:43%;font-size:3.8px"><i class="dot" style="width:9px;height:9px"></i><span><b style="font-weight:600">Owen Marsh</b><br><span class="hint">00:16</span></span><span class="hint" style="margin-left:auto">Yesterday</span></div>
    <div class="row" style="top:52%;font-size:3.8px"><i class="dot" style="width:9px;height:9px;background:#a2563e"></i><span><b style="font-weight:600">Nora Vale</b><br><span class="hint">Start message with Nora</span></span></div>
    <div class="row" style="top:62%;font-size:3.8px"><i class="dot b" style="width:9px;height:9px"></i><span><b style="font-weight:600">Iris Kemp</b><br><span class="hint">00:24</span></span><span class="hint" style="margin-left:auto">09:01 AM</span></div>
    <div class="row" style="top:72%;font-size:3.8px"><i class="dot" style="width:9px;height:9px"></i><span><b style="font-weight:600">Owen Marsh</b><br><span class="hint">00:16</span></span><span class="hint" style="margin-left:auto">Yesterday</span></div>
    <div class="tabs" style="bottom:7%"><i></i><i></i><i class="rec" style="width:18px;height:7px"></i><i></i><i></i></div>
    <div class="home-ind" style="bottom:1.5%"></div>
  </div>
</section>

<section class="panel violet" style="left:576px;top:894px;width:466px;height:439px">
  <div class="panel-meta" style="height:24px;padding-left:15px;font-size:8.5px">Complete / 03.02.2021 / studio.desk@mailbox.test</div>
  <div class="panel-head" style="top:24px;height:85px;padding:30px 33px">
    <h2 style="font-size:26px">Specs</h2>
  </div>
  <div class="spec-body abs" style="left:31px;top:142px;width:420px">
    <h3 style="font-size:31px">Component</h3>
    <p style="font-size:13px;margin-top:11px;line-height:1.3">The component should already exist within MobiOS but may not be up to scratch for Human Interface Guidelines. It's worth double checking.</p>
    <p class="lbl" style="font-size:13px;margin-top:19px">Details of the component can be found here:</p>
    <a style="font-size:13px;margin-top:5px">https://dev.mobios.test/platform/</a>
    <p class="lbl" style="font-size:13px;margin-top:19px">Designer Version:</p>
    <a style="font-size:13px;margin-top:5px">https://dev.mobios.test/design/interface-guidelines/platform</a>
  </div>
</section>

<!-- ============ SECTION 3: Homescreen ============ -->
<div class="title-bar" style="left:54px;top:1440px;width:1076px;height:55px;padding-left:20px;font-size:15px">[UI SCREEN] Homescreen with 2 vertical rows of Avatars with name of contacts (first and last name)</div>

<section class="panel violet" style="left:54px;top:1515px;width:549px;height:859px">
  <div class="panel-meta" style="height:14px;padding-left:17px;font-size:5.5px">Complete / 04.02.2021 / studio.desk@mailbox.test</div>
  <div class="panel-head" style="top:14px;height:53px;padding:18px 20px">
    <h2 style="font-size:16px">User Flows</h2>
  </div>

  <svg class="arrows" width="549" height="859" aria-hidden="true">
    <defs><marker id="a3" viewBox="0 0 6 6" refX="5" refY="3" markerWidth="4" markerHeight="4" orient="auto"><path d="M0 0L6 3L0 6z" fill="#39b86a"/></marker></defs>
    <g fill="none" stroke="#39b86a" stroke-width=".7" marker-end="url(#a3)">
      <polyline points="58,142 112,142 112,204 161,204"/>
      <line x1="191" y1="220" x2="191" y2="315"/>
      <line x1="334" y1="220" x2="334" y2="315"/>
      <line x1="477" y1="220" x2="477" y2="315"/>
      <polyline points="455,228 455,210 500,210"/>
      <line x1="455" y1="315" x2="455" y2="228"/>
      <polyline points="356,345 390,345 390,360 447,360"/>
      <polyline points="161,497 95,497 95,505 78,505"/>
      <polyline points="186,530 125,530 125,560 78,560"/>
      <polyline points="219,530 256,530 256,560 304,560"/>
      <polyline points="210,522 270,522 270,497 304,497"/>
    </g>
    <text x="96" y="555" font-size="4.5" fill="#333" font-family="Inter,sans-serif">Swiped Left</text>
    <text x="262" y="555" font-size="4.5" fill="#333" font-family="Inter,sans-serif">Swiped Right</text>
  </svg>

  <!-- home screen template repeated -->
  <div class="ph" style="left:18px;top:104px;width:60px;height:133px">
    <div class="sb"><span>9:41</span><span>•••</span></div>
    <div class="tx" style="top:7%;font-weight:600">Home</div>
    <div class="tx" style="top:12%;font-weight:600">Recent Message</div>
    <div class="tx hint" style="top:15.5%;font-size:2.5px">Tap to record / play a message</div>
    <div class="av" style="left:12px;top:21%;width:14px;height:14px"></div>
    <div class="av" style="left:35px;top:21%;width:14px;height:14px"></div>
    <div class="av" style="left:12px;top:41%;width:14px;height:14px"></div>
    <div class="av hl" style="left:35px;top:41%;width:14px;height:14px"></div>
    <div class="row" style="top:61%"><b style="font-weight:600">Contact</b><span class="blue-t" style="margin-left:auto">View All</span></div>
    <div class="row" style="top:66%"><i class="dot"></i>Nora Vale</div>
    <div class="row" style="top:75%"><i class="dot b"></i>Iris Kemp</div>
    <div class="row" style="top:84%"><i class="dot"></i>Owen Marsh</div>
    <div class="tabs"><i></i><i></i><i class="rec"></i><i></i><i></i></div>
  </div>
  <div class="ph" style="left:161px;top:104px;width:60px;height:133px">
    <div class="sb"><span>9:41</span><span>•••</span></div>
    <div class="tx" style="top:7%;font-weight:600">Home</div>
    <div class="tx" style="top:12%;font-weight:600">Recent Message</div>
    <div class="tx hint" style="top:15.5%;font-size:2.5px">Tap to record / play a message</div>
    <div class="av" style="left:12px;top:21%;width:14px;height:14px"></div>
    <div class="av" style="left:35px;top:21%;width:14px;height:14px"></div>
    <div class="av" style="left:12px;top:41%;width:14px;height:14px"></div>
    <div class="av hl" style="left:35px;top:41%;width:14px;height:14px"></div>
    <div class="row" style="top:61%"><b style="font-weight:600">Contact</b><span class="blue-t" style="margin-left:auto">View All</span></div>
    <div class="row" style="top:66%"><i class="dot"></i>Nora Vale</div>
    <div class="row" style="top:75%"><i class="dot k"></i>00:43</div>
    <div class="row" style="top:84%"><i class="dot"></i>Owen Marsh</div>
    <div class="tabs"><i></i><i></i><i class="rec"></i><i></i><i></i></div>
  </div>
  <div class="ph" style="left:304px;top:104px;width:60px;height:133px">
    <div class="sb"><span>9:41</span><span>•••</span></div>
    <div class="tx" style="top:7%;font-weight:600">Home</div>
    <div class="tx" style="top:12%;font-weight:600">Recent Message</div>
    <div class="tx hint" style="top:15.5%;font-size:2.5px">Tap to record / play a message</div>
    <div class="av" style="left:12px;top:21%;width:14px;height:14px"></div>
    <div class="av" style="left:35px;top:21%;width:14px;height:14px"></div>
    <div class="av" style="left:12px;top:41%;width:14px;height:14px"></div>
    <div class="av hl" style="left:35px;top:41%;width:14px;height:14px"></div>
    <div class="row" style="top:61%"><b style="font-weight:600">Contact</b><span class="blue-t" style="margin-left:auto">View All</span></div>
    <div class="row" style="top:66%"><i class="dot"></i>Nora Vale</div>
    <div class="row" style="top:75%"><i class="dot k"></i>00:27</div>
    <div class="row" style="top:84%"><i class="dot"></i>Owen Marsh</div>
    <div class="tabs"><i></i><i></i><i class="rec"></i><i></i><i></i></div>
  </div>
  <div class="ph" style="left:447px;top:104px;width:60px;height:133px">
    <div class="sb"><span>9:41</span><span>•••</span></div>
    <div class="tx" style="top:7%;font-weight:600">Home</div>
    <div class="tx" style="top:12%;font-weight:600">Recent Message</div>
    <div class="tx hint" style="top:15.5%;font-size:2.5px">Tap to record / play a message</div>
    <div class="av" style="left:12px;top:21%;width:14px;height:14px"></div>
    <div class="av" style="left:35px;top:21%;width:14px;height:14px"></div>
    <div class="av" style="left:12px;top:41%;width:14px;height:14px"></div>
    <div class="av hl" style="left:35px;top:41%;width:14px;height:14px"></div>
    <div class="row" style="top:61%"><b style="font-weight:600">Contact</b><span class="blue-t" style="margin-left:auto">View All</span></div>
    <div class="row" style="top:66%"><i class="dot"></i>Nora Vale</div>
    <div class="row" style="top:75%"><i class="dot" style="background:var(--pink)"></i>00:16</div>
    <div class="row" style="top:84%"><i class="dot"></i>Owen Marsh</div>
    <div class="tabs"><i></i><i></i><i class="rec"></i><i></i><i></i></div>
  </div>

  <!-- playing / recording -->
  <div class="ph" style="left:161px;top:315px;width:60px;height:133px">
    <div class="sb"><span>9:41</span><span>•••</span></div>
    <div class="tx" style="top:7%;font-weight:600">Playing</div>
    <div class="av" style="left:18px;top:12%;width:24px;height:24px;background:#5a5c60"></div>
    <div class="tx" style="top:33%;font-weight:600">Theo Lindqvist</div>
    <div class="row" style="top:42%"><i class="dot k"></i>00:43<span style="margin-left:auto">Done</span></div>
    <div class="ln" style="left:4%;width:50%;top:53%"></div>
    <div class="row" style="top:58%;color:var(--pink)">3 New Messages</div>
    <div class="row" style="top:64%">Voice Message<i class="dot k" style="margin-left:auto"></i></div>
    <div class="row" style="top:72%">Voice Message<i class="dot k" style="margin-left:auto"></i></div>
    <div class="glow" style="top:86%"></div>
  </div>
  <div class="ph" style="left:304px;top:315px;width:60px;height:133px">
    <div class="sb"><span>9:41</span><span>•••</span></div>
    <div class="tx" style="top:7%;font-weight:600">Playing</div>
    <div class="av" style="left:18px;top:12%;width:24px;height:24px;background:#5a5c60"></div>
    <div class="tx" style="top:33%;font-weight:600">Theo Lindqvist</div>
    <div class="row" style="top:42%"><i class="dot k"></i>00:27<span style="margin-left:auto">Done</span></div>
    <div class="ln" style="left:4%;width:50%;top:53%"></div>
    <div class="row" style="top:58%;color:var(--pink)">1 New Message</div>
    <div class="row" style="top:64%">Voice Message<i class="dot k" style="margin-left:auto"></i></div>
    <div class="glow" style="top:86%"></div>
  </div>
  <div class="ph" style="left:447px;top:315px;width:60px;height:133px">
    <div class="sb"><span>9:41</span><span>•••</span></div>
    <div class="tx" style="top:7%;font-weight:600">Recording</div>
    <div class="av" style="left:18px;top:12%;width:24px;height:24px;background:#5a5c60"></div>
    <div class="tx" style="top:33%;font-weight:600">Theo Lindqvist</div>
    <div class="row" style="top:42%"><i class="dot" style="background:var(--pink)"></i>00:16<span style="margin-left:auto">Stop</span></div>
    <div class="tx" style="top:50%;color:var(--pink)">Delete</div>
    <div class="row" style="top:58%">Recent Sent Message</div>
    <div class="row" style="top:64%">Voice Message<i class="dot k" style="margin-left:auto"></i></div>
    <div class="glow" style="top:86%"></div>
  </div>

  <!-- swipe row -->
  <div class="ph" style="left:18px;top:477px;width:60px;height:133px">
    <div class="nav" style="top:3%"><span>‹ Back</span><b>Theo Lindqvist</b><span></span></div>
    <div class="av sm" style="left:3px;top:15%;width:5px;height:5px"></div>
    <div class="ln" style="left:12%;width:70%;top:16%"></div><div class="ln" style="left:12%;width:64%;top:19%"></div><div class="ln" style="left:12%;width:58%;top:22%"></div>
    <div class="av sm" style="right:3px;top:29%;width:5px;height:5px;background:#a2563e"></div>
    <div class="ln" style="left:8%;width:70%;top:30%"></div><div class="ln" style="left:8%;width:60%;top:33%"></div>
    <div class="ln" style="left:8%;width:40%;top:40%"></div>
    <div class="emo" style="top:81%"><i></i><i></i><i></i><i></i></div>
    <div class="tabs" style="bottom:3%"><i></i><i></i><i></i></div>
  </div>
  <div class="ph" style="left:161px;top:477px;width:60px;height:133px">
    <div class="sb"><span>9:41</span><span>•••</span></div>
    <div class="tx" style="top:7%;font-weight:600">Home</div>
    <div class="tx" style="top:12%;font-weight:600">Recent Message</div>
    <div class="av" style="left:12px;top:21%;width:14px;height:14px"></div>
    <div class="av" style="left:35px;top:21%;width:14px;height:14px"></div>
    <div class="av" style="left:12px;top:41%;width:14px;height:14px"></div>
    <div class="av hl" style="left:35px;top:41%;width:14px;height:14px"></div>
    <div class="row" style="top:61%"><b style="font-weight:600">Contact</b><span class="blue-t" style="margin-left:auto">View All</span></div>
    <div class="row" style="top:66%"><i class="dot"></i>Nora Vale</div>
    <div class="row" style="top:75%"><i class="dot b"></i>Iris Kemp</div>
    <div class="row" style="top:84%"><i class="dot"></i>Owen Marsh</div>
    <div class="tabs"><i></i><i></i><i class="rec"></i><i></i><i></i></div>
  </div>
  <div class="ph" style="left:304px;top:477px;width:60px;height:133px">
    <div class="nav" style="top:3%"><span>‹ Back</span><b>Mira Stone</b><span></span></div>
    <div class="av sm" style="left:3px;top:15%;width:5px;height:5px"></div>
    <div class="ln" style="left:12%;width:70%;top:16%"></div><div class="ln" style="left:12%;width:64%;top:19%"></div><div class="ln" style="left:12%;width:58%;top:22%"></div>
    <div class="av sm" style="right:3px;top:29%;width:5px;height:5px;background:#a2563e"></div>
    <div class="ln" style="left:8%;width:70%;top:30%"></div><div class="ln" style="left:8%;width:60%;top:33%"></div>
    <div class="ln" style="left:8%;width:40%;top:40%"></div>
    <div class="emo" style="top:81%"><i></i><i></i><i></i><i></i></div>
    <div class="tabs" style="bottom:3%"><i></i><i></i><i></i></div>
  </div>

  <!-- contacts list -->
  <div class="ph" style="left:18px;top:651px;width:60px;height:133px;font-size:2.6px">
    <div class="row" style="top:4%"><i class="dot"></i>Theo Lindqvist<span class="hint" style="margin-left:auto">Yesterday</span></div>
    <div class="row" style="top:12%"><i class="dot" style="background:#a2563e"></i>Lena Crane<span class="hint" style="margin-left:auto">Yesterday</span></div>
    <div class="row" style="top:20%"><i class="dot" style="background:#b94040"></i>Ada Brook<span class="hint" style="margin-left:auto">Yesterday</span></div>
    <div class="row" style="top:28%"><i class="dot"></i>Leo Fischer<span class="hint" style="margin-left:auto">Yesterday</span></div>
    <div class="row" style="top:36%"><i class="dot"></i>Kai Holland<span class="hint" style="margin-left:auto">Yesterday</span></div>
    <div class="row" style="top:44%"><i class="dot"></i>Iris Kemp<span class="hint" style="margin-left:auto">Yesterday</span></div>
    <div class="row" style="top:52%"><i class="dot"></i>Jude Walsh<span class="hint" style="margin-left:auto">Yesterday</span></div>
    <div class="row" style="top:60%"><i class="dot"></i>Noel Barker<span class="hint" style="margin-left:auto">Yesterday</span></div>
    <div class="row" style="top:68%"><i class="dot"></i>Rhea Quinn<span class="hint" style="margin-left:auto">Yesterday</span></div>
    <div class="row" style="top:76%"><i class="dot" style="background:var(--pink)"></i>00:16<span class="hint" style="margin-left:auto">Stop</span></div>
    <div class="row" style="top:86%"><i class="dot"></i>Owen Marsh<span class="hint" style="margin-left:auto">Yesterday</span></div>
  </div>
</section>

<section class="panel violet" style="left:622px;top:1515px;width:234px;height:289px">
  <div class="panel-meta" style="height:14px;padding-left:8px;font-size:5.5px">Complete / 04.02.2021 / studio.desk@mailbox.test</div>
  <div class="panel-head" style="top:14px;height:53px;padding:18px 19px">
    <h2 style="font-size:16px">Specs</h2>
  </div>
  <div class="spec-body abs" style="left:19px;top:83px;width:200px">
    <h3 style="font-size:20px">Component</h3>
    <p style="font-size:8px;margin-top:6px;line-height:1.3">The component should already exist within MobiOS but may not be up to scratch for Human Interface Guidelines. It's worth double checking.</p>
    <p class="lbl" style="font-size:8px;margin-top:12px">Details of the component can be found here:</p>
    <a style="font-size:8px;margin-top:2px">https://dev.mobios.test/platform/</a>
    <p class="lbl" style="font-size:8px;margin-top:12px">Designer Version:</p>
    <a style="font-size:8px;margin-top:2px;line-height:1.3">https://dev.mobios.test/design/interface-guidelines/platform</a>
  </div>
</section>

<section class="panel violet" style="left:873px;top:1515px;width:257px;height:627px">
  <div class="panel-meta" style="height:14px;padding-left:8px;font-size:5.5px">Complete / 04.02.2021 / studio.desk@mailbox.test</div>
  <div class="panel-head" style="top:14px;height:53px;padding:18px 20px">
    <h2 style="font-size:16px">States</h2>
  </div>

  <svg class="arrows" width="257" height="627" aria-hidden="true">
    <g fill="none" stroke="#39b86a" stroke-width=".7">
      <line x1="55" y1="90" x2="55" y2="133"/>
      <line x1="60" y1="148" x2="83" y2="148"/>
      <line x1="60" y1="302" x2="83" y2="302"/>
      <line x1="40" y1="370" x2="83" y2="370"/>
      <line x1="17" y1="370" x2="17" y2="405"/>
      <line x1="60" y1="488" x2="83" y2="488"/>
    </g>
  </svg>
  <div class="num" style="left:51px;top:83px">1</div>
  <div class="num" style="left:83px;top:144px">2</div>
  <div class="num" style="left:83px;top:298px">3</div>
  <div class="num" style="left:83px;top:366px">4</div>
  <div class="num" style="left:13px;top:405px">5</div>
  <div class="num" style="left:83px;top:484px">5</div>

  <div class="ph" style="left:13px;top:105px;width:60px;height:133px">
    <div class="sb"><span>9:41</span><span>•••</span></div>
    <div class="tx" style="top:7%;font-weight:600">Home</div>
    <div class="tx" style="top:12%;font-weight:600">Recent Message</div>
    <div class="av" style="left:12px;top:21%;width:14px;height:14px"></div>
    <div class="av" style="left:35px;top:21%;width:14px;height:14px"></div>
    <div class="av" style="left:12px;top:41%;width:14px;height:14px"></div>
    <div class="av hl" style="left:35px;top:41%;width:14px;height:14px"></div>
    <div class="row" style="top:61%"><b style="font-weight:600">Contact</b><span class="blue-t" style="margin-left:auto">View All</span></div>
    <div class="row" style="top:66%"><i class="dot"></i>Nora Vale</div>
    <div class="row" style="top:75%"><i class="dot b"></i>Iris Kemp</div>
    <div class="row" style="top:84%"><i class="dot"></i>Owen Marsh</div>
    <div class="tabs"><i></i><i></i><i class="rec"></i><i></i><i></i></div>
  </div>
  <div class="ph" style="left:13px;top:262px;width:60px;height:133px">
    <div class="sb"><span>9:41</span><span>•••</span></div>
    <div class="tx" style="top:7%;font-weight:600">Home</div>
    <div class="tx" style="top:12%;font-weight:600">Recent Message</div>
    <div class="av" style="left:12px;top:21%;width:14px;height:14px"></div>
    <div class="av" style="left:35px;top:21%;width:14px;height:14px"></div>
    <div class="av" style="left:12px;top:41%;width:14px;height:14px"></div>
    <div class="av hl" style="left:35px;top:41%;width:14px;height:14px"></div>
    <div class="row" style="top:61%"><b style="font-weight:600">Contact</b><span class="blue-t" style="margin-left:auto">View All</span></div>
    <div class="row" style="top:66%"><i class="dot"></i>Nora Vale</div>
    <div class="row" style="top:75%"><i class="dot k"></i>00:43</div>
    <div class="row" style="top:84%"><i class="dot"></i>Owen Marsh</div>
    <div class="tabs"><i></i><i></i><i class="rec"></i><i></i><i></i></div>
  </div>
  <div class="ph" style="left:13px;top:449px;width:60px;height:133px">
    <div class="sb"><span>9:41</span><span>•••</span></div>
    <div class="tx" style="top:7%;font-weight:600">Home</div>
    <div class="tx" style="top:12%;font-weight:600">Recent Message</div>
    <div class="av" style="left:12px;top:21%;width:14px;height:14px"></div>
    <div class="av" style="left:35px;top:21%;width:14px;height:14px"></div>
    <div class="av" style="left:12px;top:41%;width:14px;height:14px"></div>
    <div class="av hl" style="left:35px;top:41%;width:14px;height:14px"></div>
    <div class="row" style="top:61%"><b style="font-weight:600">Contact</b><span class="blue-t" style="margin-left:auto">View All</span></div>
    <div class="row" style="top:66%"><i class="dot"></i>Nora Vale</div>
    <div class="row" style="top:75%"><i class="dot" style="background:var(--pink)"></i>00:16</div>
    <div class="row" style="top:84%"><i class="dot"></i>Owen Marsh</div>
    <div class="tabs"><i></i><i></i><i class="rec"></i><i></i><i></i></div>
  </div>

  <div class="note" style="left:123px;top:110px;width:117px;height:58px"><b>Element Name:</b>Avatar<br><br><b>Notes:</b>"Single Tab" to open Bottom Screen and Record or Play Message</div>
  <div class="note" style="left:123px;top:177px;width:117px;height:55px"><b>Element Name:</b>Recording Feature<br><br><b>Notes:</b>New message will play first before the recording feature is activated</div>
  <div class="note" style="left:123px;top:270px;width:117px;height:55px"><b>Element Name:</b>Toggle Play Button<br><br><b>Notes:</b>Tab again to stop playing message &amp; toggle message as played.</div>
  <div class="note" style="left:123px;top:336px;width:117px;height:55px"><b>Element Name:</b>Expand Button<br><br><b>Notes:</b>Tab "Expand Button" to expand or collapse parent or child rows</div>
  <div class="note" style="left:123px;top:454px;width:117px;height:55px"><b>Element Name:</b>Recording<br><br><b>Notes:</b>Tab "Record" Button to start recording new message</div>
</section>

</body>
</html>
```